Brightmark Pixel Collective Website

I need my website redesigned to look very modern with the latest services. Check out my old website for information: www.brightmarkpixelcollective.com

You can use the same site menu links

It doesn't need to have the Recent News section

Please use the yellow, black and grey color scheme

Target Market(s)

25-50 years in range. Small Business Owners

Industry/Entity Type

Group

Requirements
Must have
• Logo and similar color scheme to current website
• Modern, Modern, Modern! I want a very fresh and modern look
Should not have
• Boring Look

```html
<!DOCTYPE html>
<html lang="en">
<head>
<meta charset="utf-8">
<title>Brightmark Pixel Collective</title>
<link href="https://fonts.googleapis.com/css2?family=Open+Sans:wght@300;400;600;700&display=swap" rel="stylesheet">
<style>
:root{
  --black:#000;
  --yellow:#ffcc00;
  --yellow-deep:#ffb400;
  --yellow-light:#ffd24a;
  --band:#ffd200;
  --white:#fff;
  --grey:#d8d8d8;
  --muted:#5a4a10;
  --caption:#fff3b0;
}
*{margin:0;padding:0;box-sizing:border-box}
html,body{width:1039px;height:1200px;overflow:hidden;background:var(--black)}
body{font-family:"Open Sans",Arial,sans-serif;color:var(--white);position:relative}
a{color:inherit;text-decoration:none}
.abs{position:absolute}

/* header */
.site-header{position:absolute;left:0;top:0;width:1039px;height:100px;background:var(--black)}
.brand{position:absolute;left:163px;top:26px;display:flex;align-items:center;gap:8px}
.brand-square{width:22px;height:22px;background:var(--yellow)}
.brand-name{font-size:13px;font-weight:400;line-height:16px;color:var(--grey);width:120px}
.contact-line{position:absolute;left:433px;top:24px;font-size:12px;font-weight:700}
.contact-line span{margin:0 8px}
.estimate-btn{position:absolute;left:720px;top:22px;width:148px;height:22px;background:var(--yellow);color:var(--white);font-size:10.5px;font-weight:700;text-align:center;line-height:22px}
.main-nav{position:absolute;left:400px;top:67px;display:flex;height:33px;font-size:12.5px}
.main-nav a{padding:0 13px;line-height:44px}
.main-nav a.active{background:var(--yellow);color:var(--black);border-radius:4px 4px 0 0;padding:0 17px;line-height:44px}

/* hero */
.hero{position:absolute;left:0;top:100px;width:1039px;height:317px;background:radial-gradient(ellipse at 55% 40%,var(--yellow-light),var(--yellow-deep) 85%)}
.hero-arrow{position:absolute;top:129px;width:44px;height:44px;border-radius:50%;background:rgba(255,230,150,.55)}
.hero-title{position:absolute;left:190px;top:118px;font-size:29px;font-weight:400;color:#2a1d00}
.hero-shot{position:absolute;left:452px;top:72px;width:386px;height:225px;background:linear-gradient(90deg,#6a1f1a 0%,#3a2a2a 14%,#f4f4f4 24%,#e9eef6 76%,#3a4b7a 88%,#b3b9c7 100%);box-shadow:0 18px 26px rgba(120,70,0,.35)}

/* features */
.features{position:absolute;left:0;top:417px;width:1039px;height:284px;background:var(--black)}
.feature{position:absolute;top:36px;width:232px;height:200px}
.feature-head{display:flex;align-items:center;gap:10px;height:42px}
.feature-title{font-size:14px;font-weight:600;color:var(--yellow)}
.feature-sub{position:absolute;top:54px;left:0;width:232px;font-size:11px;font-weight:700;line-height:18px}
.feature-body{position:absolute;top:99px;left:0;width:232px;font-size:10.5px;font-weight:300;line-height:18px;color:#eee}
.read-more{position:absolute;top:246px;display:flex;align-items:center;gap:6px;font-size:9.5px;font-weight:600}

/* recent works */
.recent{position:absolute;left:0;top:701px;width:1039px;height:236px;background:var(--band)}
.recent-title{position:absolute;left:0;width:1039px;top:24px;text-align:center;font-size:14px;font-weight:600;color:var(--muted)}
.work{position:absolute;top:62px;width:180px;text-align:center}
.work-thumb{margin:0 auto;height:96px}
.work-name{margin-top:14px;font-size:10.5px;font-weight:700;color:var(--white)}
.work-type{font-size:10.5px;color:var(--caption);line-height:18px}
.work-url{font-size:10.5px;color:#2a1d00;line-height:18px}

/* footer */
.site-footer{position:absolute;left:0;top:937px;width:1039px;height:263px;background:var(--black)}
.footer-col{position:absolute;top:32px;font-size:9px}
.footer-col h4{font-size:9.5px;font-weight:700;margin-bottom:32px}
.footer-col li{list-style:none;line-height:22px;font-weight:400}
.social-box{position:absolute;left:707px;top:29px;width:161px;height:118px;background:var(--white);padding:3px}
.social-box-top{height:42px;background:var(--black);display:flex;align-items:center;gap:5px;padding-left:10px}
.social-box-top .sq{width:10px;height:10px;background:var(--yellow)}
.social-box-top .nm{font-size:7px;color:var(--grey)}
.social-box p{font-size:6px;color:#333;margin:6px 0 0 6px}
.faces{display:flex;gap:4px;margin:6px 0 0 7px}
.faces span{width:26px;height:26px;background:linear-gradient(#c9b7a6,#7d6c63)}
.social-box small{display:block;font-size:5px;color:#4a5a8a;margin:5px 0 0 7px}
.social-icons{position:absolute;left:799px;top:163px;display:flex;gap:2px}
.social-icons span{width:21px;height:21px;border-radius:3px}
.footer-brand{position:absolute;left:173px;top:192px;display:flex;align-items:center;gap:6px}
.footer-brand .sq{width:14px;height:14px;background:var(--yellow)}
.footer-brand .nm{font-size:8.5px;color:var(--grey);width:90px;line-height:11px}
.footer-links{position:absolute;left:387px;top:199px;font-size:9px}
.footer-links .city{margin-right:16px}
.copyright{position:absolute;left:657px;top:222px;font-size:9px;letter-spacing:-.2px}
</style>
</head>
<body>

<header class="site-header">
  <div class="brand"><span class="brand-square"></span><span class="brand-name">Brightmark Pixel Collective</span></div>
  <div class="contact-line">Local: 612-555-0148<span>|</span>Toll Free: 1-800-555-0172</div>
  <a class="estimate-btn" href="#">Request Free Estimate</a>
  <nav class="main-nav">
    <a class="active" href="#">Home</a>
    <a href="#">Web Design</a>
    <a href="#">Search Engine Marketing</a>
    <a href="#">Social Media</a>
    <a href="#">Contact</a>
  </nav>
</header>

<section class="hero">
  <span class="hero-arrow" style="left:103px"><svg width="44" height="44" viewBox="0 0 44 44"><path d="M25 13 L16 22 L25 31" fill="none" stroke="#ffb000" stroke-width="4" stroke-linecap="round" stroke-linejoin="round"/></svg></span>
  <h1 class="hero-title">Web Desigining</h1>
  <div class="hero-shot" role="img" aria-label="Stack of website screenshots fanned out in perspective"></div>
  <span class="hero-arrow" style="left:891px"><svg width="44" height="44" viewBox="0 0 44 44"><path d="M19 13 L28 22 L19 31" fill="none" stroke="#ffb000" stroke-width="4" stroke-linecap="round" stroke-linejoin="round"/></svg></span>
</section>

<section class="features">
  <article class="feature" style="left:170px">
    <div class="feature-head">
      <svg width="42" height="38" viewBox="0 0 42 38"><path d="M0 0 L42 15 L22 18 Z" fill="#fff"/><path d="M0 0 L22 18 L18 36 Z" fill="#fff"/><path d="M22 18 L28 28 L18 36 Z" fill="#ccc"/></svg>
      <h2 class="feature-title">Our Mission</h2>
    </div>
    <p class="feature-sub">Brightmark Pixel Collective will get you noticed</p>
    <p class="feature-body">We are an award winning web design &amp; internet marketing company located in Lakeport. As a Lakeport Web Design company, we create web sites to what our clients want and that's found in our marketing. Here at Brightmark Pixel Collective</p>
  </article>
  <a class="read-more" href="#" style="left:170px">Read More <svg width="14" height="14" viewBox="0 0 14 14"><circle cx="7" cy="7" r="7" fill="#fff"/><path d="M6 4 L9 7 L6 10" fill="none" stroke="#000" stroke-width="1.8"/></svg></a>

  <article class="feature" style="left:408px">
    <div class="feature-head">
      <svg width="46" height="40" viewBox="0 0 46 40"><rect x="1" y="1" width="44" height="28" rx="3" fill="none" stroke="#fff" stroke-width="2.5"/><rect x="1" y="22" width="44" height="7" fill="#fff"/><rect x="20" y="29" width="6" height="6" fill="#fff"/><rect x="14" y="35" width="18" height="3" fill="#fff"/></svg>
      <h2 class="feature-title">Internet Marketing</h2>
    </div>
    <p class="feature-sub">Home of the "Pay for Performance" Guarantee</p>
    <p class="feature-body">You've invested countless hours and a large sum of money to build your online presence, why waste the investment by not marketing it? Even if you've built it to give your current customers information about your business... don't you want more local</p>
  </article>
  <a class="read-more" href="#" style="left:409px">Read More <svg width="14" height="14" viewBox="0 0 14 14"><circle cx="7" cy="7" r="7" fill="#fff"/><path d="M6 4 L9 7 L6 10" fill="none" stroke="#000" stroke-width="1.8"/></svg></a>

  <article class="feature" style="left:647px">
    <div class="feature-head">
      <svg width="46" height="40" viewBox="0 0 46 40"><rect x="1.5" y="2" width="43" height="36" rx="2" fill="none" stroke="#fff" stroke-width="2.5"/><rect x="1.5" y="2" width="43" height="6" fill="#fff"/><circle cx="6" cy="5" r="1.2" fill="#000"/><circle cx="10" cy="5" r="1.2" fill="#000"/><circle cx="14" cy="5" r="1.2" fill="#000"/></svg>
      <h2 class="feature-title">Website Design</h2>
    </div>
    <p class="feature-sub">A Rewarding Experience</p>
    <p class="feature-body">Welcome to Brightmark Pixel Collective. We are very excited and proud to help you achieve the internet solution that you need. We have an experienced team of web designers, developers, graphic designers, SEO specialist, social networking professionals</p>
  </article>
  <a class="read-more" href="#" style="left:647px">Read More <svg width="14" height="14" viewBox="0 0 14 14"><circle cx="7" cy="7" r="7" fill="#fff"/><path d="M6 4 L9 7 L6 10" fill="none" stroke="#000" stroke-width="1.8"/></svg></a>
</section>

<section class="recent">
  <svg class="abs" style="left:170px;top:26px" width="16" height="22" viewBox="0 0 16 22"><path d="M12 2 L4 11 L12 20" fill="none" stroke="#fff" stroke-width="3.5"/></svg>
  <h2 class="recent-title">Recent Works</h2>
  <svg class="abs" style="left:853px;top:26px" width="16" height="22" viewBox="0 0 16 22"><path d="M4 2 L12 11 L4 20" fill="none" stroke="#fff" stroke-width="3.5"/></svg>

  <div class="work" style="left:161px">
    <div class="work-thumb" role="img" aria-label="Website thumbnail for an outdoor sporting fair" style="width:144px;background:linear-gradient(#b64a12,#7a2a10)"></div>
    <p class="work-name">Harlow Creek Fire Department</p><p class="work-type">Web Design</p><p class="work-url">www.harlowcreekfire.com</p>
  </div>
  <div class="work" style="left:339px">
    <div class="work-thumb" role="img" aria-label="Website thumbnail for a kennel business" style="width:140px;background:linear-gradient(#8a7a3a,#3d3a1c)"></div>
    <p class="work-name">Harlow Creek Fire Department</p><p class="work-type">Web Design</p><p class="work-url">www.harlowcreekfire.com</p>
  </div>
  <div class="work" style="left:521px">
    <div class="work-thumb" role="img" aria-label="Website thumbnail for a roofing company" style="width:128px;background:linear-gradient(#1b3e6e,#0f2444)"></div>
    <p class="work-name">Harlow Creek Fire Department</p><p class="work-type">Web Design</p><p class="work-url">www.harlowcreekfire.com</p>
  </div>
  <div class="work" style="left:700px">
    <div class="work-thumb" role="img" aria-label="Website thumbnail for a landscaping company" style="width:139px;background:linear-gradient(#1a1a1a 0%,#3b5a2e 35%,#596b45 100%)"></div>
    <p class="work-name">Harlow Creek Fire Department</p><p class="work-type">Web Design</p><p class="work-url">www.harlowcreekfire.com</p>
  </div>
</section>

<footer class="site-footer">
  <div class="footer-col" style="left:170px"><h4>Home</h4><ul><li>About</li><li>Contact</li><li>Login</li></ul></div>
  <div class="footer-col" style="left:289px"><h4>Search Engine Marketing</h4><ul><li>Local Map Listings</li><li>National SEO</li><li>Learn SEO</li></ul></div>
  <div class="footer-col" style="left:451px"><h4>Website Design</h4><ul><li>Client Controlled Website</li><li>Flash Website</li><li>Build a Website that Sells</li></ul></div>
  <div class="footer-col" style="left:585px"><h4>Graphic Design</h4><ul><li>Business Card Design</li><li>Logo Design</li><li>Flash Design</li></ul></div>

  <div class="social-box">
    <div class="social-box-top"><span class="sq"></span><span class="nm">Brightmark Pixel Collective</span></div>
    <p>You and 692 others like Brightmark.</p>
    <div class="faces" role="img" aria-label="Row of follower profile photos"><span></span><span></span><span></span><span></span><span></span></div>
    <small>Community social plugin</small>
  </div>

  <div class="social-icons"><span style="background:#3b5ea8"></span><span style="background:#3aa6de"></span><span style="background:#d6261f"></span></div>

  <div class="footer-brand"><span class="sq"></span><span class="nm">Brightmark Pixel Collective</span></div>
  <div class="footer-links"><span class="city">LAKEPORT, MINNESOTA</span> Home | Privacy Policy | Refund Policy | Terms &amp; Conditions | About | Affiliates | Contact</div>
  <div class="copyright">© 2009-2013 Brightmark Pixel Collective, Inc. All rights reserved.</div>
</footer>

</body>
</html>
```